Envelope and Stationary

I need an envelope and stationary package for my non-profit. I need to be able to download these, print, and use.

I am attached the logos, color files, and information I want on envelope and stationary.

The letter must have room on the left margin to put the list of names, Board Members, etc... I will attach a sample.

What I am looking for is to jazz this up a little bit. The Tobin Vale Children's Foundation is promotes physical fitness in children through after school programs.

Once this project is done, I need a powerpoint template, business cards, and many other pieces.

Please help me make my envelopes and letterhead standout from everyone else.

Target Market(s)

Donors, Community citizens, and prospective partners.

Industry/Entity Type

Fitness

Requirements
Must have
• 1) Logo - see attached
2) Mission Statement - "The MISSION of the TOBIN VALE FOUNDATION is to provide after school enrichment, health, and fitness programs in a safe and nurturing environment."
3) Contact information
4) Space on left Margin for Board of Directors (this space will be available for edits to add/subtract names).

5) See sample letter head: The logo and address is too small and barely visible.

6) PO BOX 315927 * Palm Hollow, Florida 32099
Phone: 877-(TVF)-2815
Email: community@tvfyouth.org
Web: www.tvfyouth.org
Nice to have
• Logo and colors have some feel or scheme across top. Something that makes the letterhead and envelope stand out.

```html
<!DOCTYPE html>
<html lang="en">
<head>
<meta charset="utf-8">
<title>Tobin Vale Children's Foundation — Letterhead and Envelope</title>
<link rel="stylesheet" href="https://fonts.googleapis.com/css2?family=Open+Sans:wght@400;600;700&family=Great+Vibes&display=swap">
<style>
  :root {
    --brand-blue: #1f6fb8;
    --brand-red: #c4202e;
    --ink: #3a3a3a;
    --ink-soft: #6b6b6b;
    --paper: #ffffff;
    --backdrop: #d9d9d9;
  }
  * { box-sizing: border-box; margin: 0; padding: 0; }
  html, body { width: 1200px; height: 801px; overflow: hidden; }
  body {
    background: var(--backdrop);
    font-family: "Open Sans", Arial, sans-serif;
    color: var(--ink);
    position: relative;
  }

  /* Letterhead */
  .letterhead {
    position: absolute;
    left: 70px; top: 30px;
    width: 524px; height: 741px;
    background: var(--paper);
    box-shadow: 0 4px 14px rgba(0,0,0,.18);
  }
  .brand-name {
    font-family: "Open Sans", Arial, sans-serif;
    font-weight: 700;
    color: var(--brand-blue);
    line-height: 1.1;
  }
  .letterhead .brand-name {
    position: absolute; left: 44px; top: 52px;
    width: 190px; font-size: 20px;
  }
  .contact-block {
    position: absolute;
    border-left: 1px solid var(--brand-blue);
    font-style: normal;
    font-size: 8px; line-height: 1.45;
    color: var(--ink-soft);
  }
  .letterhead .contact-block {
    right: 40px; top: 50px;
    padding-left: 10px;
  }
  .letter-body {
    position: absolute; left: 150px; top: 160px; width: 330px;
    font-size: 8.5px; line-height: 1.6; color: var(--ink-soft);
  }
  .letter-body .salutation { font-weight: 700; color: var(--ink); margin-bottom: 10px; }
  .letter-body p { margin-bottom: 10px; }
  .signature {
    position: absolute; left: 150px; top: 520px;
  }
  .signature .sign-name {
    font-family: "Great Vibes", cursive;
    font-size: 34px; color: var(--ink);
  }
  .signature .sign-title {
    font-size: 9px; font-weight: 700; color: var(--ink-soft); margin-top: -4px;
  }
  .mission {
    position: absolute; left: 40px; right: 40px; bottom: 40px;
    display: flex; align-items: center; gap: 12px;
  }
  .mission .bar { width: 3px; height: 26px; flex: none; }
  .mission .bar.blue { background: var(--brand-blue); }
  .mission .bar.red { background: var(--brand-red); }
  .mission p {
    font-size: 9px; line-height: 1.5; color: var(--ink); text-align: center; flex: 1;
  }

  /* Envelope */
  .envelope {
    position: absolute;
    left: 620px; top: 270px;
    width: 530px; height: 260px;
    background: var(--paper);
    box-shadow: 0 4px 14px rgba(0,0,0,.2);
    overflow: hidden;
  }
  .envelope .stripe { position: absolute; left: 0; right: 0; height: 5px; }
  .envelope .stripe.top { top: 0; background: var(--brand-blue); }
  .envelope .stripe.bottom { bottom: 0; background: var(--brand-red); }
  .envelope .brand-name {
    position: absolute; left: 30px; top: 34px;
    width: 150px; font-size: 16px;
  }
  .envelope .contact-block {
    left: 200px; top: 32px;
    padding-left: 9px; font-size: 7px;
  }
</style>
</head>
<body>

<section class="letterhead" aria-label="Letterhead">
  <div class="brand-name">Tobin Vale Children's Foundation</div>

  <address class="contact-block">
    PO BOX 315927<br>
    Palm Hollow, Florida 32099<br>
    t: 877-(TVF)-2815<br>
    community@tvfyouth.org<br>
    www.tvfyouth.org
  </address>

  <div class="letter-body">
    <p class="salutation">Lorem ipsum,</p>
    <p>Cras mattis consectetur purus sit amet fermentum. Etiam porta sem malesuada magna mollis euismod. Aenean lacinia bibendum nulla sed consectetur. Nullam quis risus eget urna mollis ornare vel eu leo. Cras justo odio, dapibus ac facilisis in, egestas eget quam.</p>
    <p>Vivamus sagittis lacus vel augue laoreet rutrum faucibus dolor auctor. Maecenas faucibus mollis interdum porta ac consectetur ac, vestibulum at eros.</p>
    <p>Donec ullamcorper nulla non metus auctor fringilla. Fusce dapibus, tellus ac cursus commodo, tortor mauris condimentum nibh, ut fermentum massa justo sit amet risus.</p>
    <p>Cum sociis natoque penatibus et magnis dis parturient montes, nascetur ridiculus mus. Nullam id dolor id nibh ultricies vehicula ut id elit.</p>
    <p>Cras mattis consectetur purus sit amet fermentum. Sed posuere consectetur est at lobortis, sagittis lacus vel augue laoreet rutrum faucibus dolor auctor.</p>
  </div>

  <div class="signature">
    <div class="sign-name">Your Name</div>
    <div class="sign-title">Company Director</div>
  </div>

  <footer class="mission">
    <span class="bar blue"></span>
    <p>The MISSION of the TOBIN VALE FOUNDATION is to provide after school enrichment,<br>health, and fitness programs in a safe and nurturing environment.</p>
    <span class="bar red"></span>
  </footer>
</section>

<section class="envelope" aria-label="Envelope">
  <span class="stripe top"></span>
  <div class="brand-name">Tobin Vale Children's Foundation</div>
  <address class="contact-block">
    PO BOX 315927<br>
    Palm Hollow, Florida 32099<br>
    t: 877-(TVF)-2815<br>
    community@tvfyouth.org<br>
    www.tvfyouth.org
  </address>
  <span class="stripe bottom"></span>
</section>

</body>
</html>
```